Business Card

Need a clean, professional, simple, but clever business card for our company LUX RIDES. We only want to see black and white colors as that reflects the branding of our company. Attaching logo. Will also consider the "sky blue" shown in our web site sample png - but use of the color should be minimal.

Lux Rides is a executive car service operating in cities throughout Africa. By operating well equipped Valdren Oster vehicles, we offer the smoothest and stylish ride in town. We aim to provide customers with a valuable experience. That’s why we make sure our patrons get picked up like a boss, travel in style, and arrive fabulous.

We need a card that says that. Likely to print on the best quality/smoothest paper available, as it must speak volumes of our business and class.

We would like the rear of the card to be all black. Perhaps we can put the web url on it, or leave it blank if it looks neater/more elegant.

Use the following contact information (as you see fit):

Lux Rides Limited
P.O. Box 47106
Dar es Salaam, Tanzania

Baraka Kilonzo
Managing Director

+255 (0) 754 829016
sales@luxrides-demo.co.tz

web url: www.luxrides-demo.co.tz
email: chauffeur@luxrides-demo.co.tz

***Winning designer will likely be commissioned for more promotional work in near future.

Target Market(s)

The target market for this card is corporate executives of top firms (financial, consulting, businessmen, etc). They are interested in high quality transportation. Our fleet is all high end Valdren Oster black cars (black exterior, black interior); and therefore, that high end quality and promptness must be reflected in the card. Also simplicity, as we we take care of all the little details behind the scene.

Industry/Entity Type

Business

Requirements
Must have
• Font must be: Helvetica Neue, like the logo. You may use other variations (Thin, Ultra thin, Regular, Bold), so long as it looks and prints well.

If web url is included on the back of the card, then do NOT include it also on the front.
Nice to have
• If there is something nice and clever that you can do/think of that doesn't make the card look busy, but adds a little "posh", then I could be even more interested.

However, if there's no little thing do be done, I'd rather a simple, but very professional looking card that attracts a lot of attention.

```html
<!DOCTYPE html>
<html lang="en">
<head>
<meta charset="utf-8">
<title>Lux Rides — Business Card</title>
<link rel="stylesheet" href="https://fonts.googleapis.com/css2?family=Didact+Gothic&family=Inter:wght@400;700&display=swap">
<style>
  :root {
    --backdrop: #3b3c40;
    --card: #272a37;
    --band: #0a0a0c;
    --sky: #2ec4f1;
    --white: #ffffff;
    --rule: #4a4d58;
    --muted: #d8dae0;
  }
  * { box-sizing: border-box; margin: 0; padding: 0; }
  html, body {
    width: 1200px;
    height: 735px;
    overflow: hidden;
    background: var(--backdrop);
  }
  .stage {
    position: relative;
    width: 1200px;
    height: 735px;
    display: flex;
    align-items: center;
    justify-content: center;
    gap: 40px;
  }
  .card {
    position: relative;
    width: 540px;
    height: 309px;
    background: var(--card);
    overflow: hidden;
    box-shadow: 0 10px 28px rgba(0, 0, 0, 0.45);
  }

  /* Back side */
  .card-back {
    display: flex;
    flex-direction: column;
    align-items: center;
    justify-content: center;
  }
  .brand-name {
    font-family: "Inter", sans-serif;
    font-weight: 700;
    font-size: 40px;
    letter-spacing: 0.5px;
    color: var(--white);
    line-height: 1;
    padding: 8px 14px;
  }
  .web-strip {
    margin-top: 6px;
    width: 250px;
    height: 30px;
    background: linear-gradient(90deg, rgba(0,0,0,0.15), rgba(0,0,0,0.75) 50%, rgba(0,0,0,0.15));
    display: flex;
    align-items: center;
    justify-content: center;
    font-family: "Didact Gothic", sans-serif;
    font-size: 15px;
    color: var(--white);
    letter-spacing: 0.3px;
  }

  /* Front side */
  .identity {
    position: absolute;
    top: 92px;
    left: 0;
    right: 0;
    text-align: center;
  }
  .person-name {
    font-family: "Didact Gothic", sans-serif;
    font-size: 38px;
    color: var(--white);
    letter-spacing: 0.5px;
    line-height: 1.1;
  }
  .person-role {
    margin-top: 6px;
    font-family: "Inter", sans-serif;
    font-weight: 700;
    font-size: 13px;
    color: var(--white);
  }
  .contact-band {
    position: absolute;
    left: 0;
    right: 0;
    bottom: 11px;
    height: 62px;
    background: var(--band);
    display: flex;
  }
  .contact-item {
    flex: 1;
    display: flex;
    align-items: center;
    justify-content: center;
    text-align: center;
    font-family: "Didact Gothic", sans-serif;
    font-size: 13px;
    line-height: 1.35;
    color: var(--muted);
    border-left: 1px solid var(--rule);
  }
  .contact-item:first-child { border-left: none; }
  .accent-strip {
    position: absolute;
    left: 0;
    right: 0;
    bottom: 0;
    height: 11px;
    background: var(--sky);
  }
</style>
</head>
<body>
  <main class="stage">
    <section class="card card-back" aria-label="Card back">
      <div class="brand-name">LUX RIDES</div>
      <div class="web-strip">www.luxrides-demo.co.tz</div>
    </section>

    <section class="card card-front" aria-label="Card front">
      <div class="identity">
        <h1 class="person-name">Baraka Kilonzo</h1>
        <p class="person-role">Managing Director</p>
      </div>
      <div class="contact-band">
        <div class="contact-item contact-phone">+255 (0) 754 829016</div>
        <div class="contact-item contact-email">sales@luxrides-demo.co.tz</div>
        <div class="contact-item contact-address">P.O. Box 47106,<br>Dar es Salaam, Tanzania</div>
      </div>
      <div class="accent-strip"></div>
    </section>
  </main>
</body>
</html>
```